Business card for Autism Consultancy

I need a double-sided business card for Brightpath Learning Consultancy
Please try to use the colours and graphics in line with our website www.brightpathlearn.nz
Front side
Logo and the name of the company – Brightpath Learning Consultancy
We use Child-Centred, Modern and Innovative approaches
Teaching autistic children to bond, laugh and play
www.brightpathlearn.nz
info@brightpathlearn.nz
phone +64 09 37 615 48
Back side
Photo
Mirela Dunstan
Founder
Postgraduate Autism (Children) Specialist (with Merit)
Qualified by the Faculty of Learning Support and Access Studies (FLSA), Harwell Vale University
mirela@brightpathlearn.nz
phone +64 937 615 48
mobile: +64 20 6283 9150
Please do not convert the text fields to outlines, i.e. I need to be able to edit any text after.
The final design should be either in Adobe Illustrator or Adobe Photoshop format.
The Specs for the business card are:
Full Bleed Size
94 x 58 mm
1110 x 685 pixels
Document Trim Size
91 x 55 mm
1075 x 650 pixels

```html
<!DOCTYPE html>
<html lang="en">
<head>
<meta charset="utf-8">
<title>Brightpath Learning Consultancy – Business Card</title>
<link rel="stylesheet" href="https://fonts.googleapis.com/css2?family=Germania+One&family=Mulish:wght@500;600;700&display=swap">
<style>
  :root {
    --navy: #1e2f5e;
    --yellow: #f6c81c;
    --paper: #fbfbfb;
    --band-text: #e3e7f0;
    --grey: #8a8f99;
    --page: #ececec;
    --display: "Germania One", fantasy;
    --body: "Mulish", sans-serif;
  }
  * { box-sizing: border-box; margin: 0; padding: 0; }
  html, body { width: 1200px; height: 800px; overflow: hidden; background: var(--page); }
  .canvas {
    position: relative; width: 1200px; height: 800px;
    font-family: var(--body);
  }
  .card {
    position: absolute; top: 243px; width: 520px; height: 314px;
    background: var(--paper); overflow: hidden;
    box-shadow: 0 6px 18px rgba(0,0,0,0.12);
  }
  .card--front { left: 50px; }
  .card--back { left: 630px; }

  .band { position: absolute; left: 0; width: 100%; height: 157px; background: var(--navy); }
  .card--front .band { bottom: 0; }
  .card--back .band { top: 0; }

  /* front */
  .brand { position: absolute; left: 40px; top: 56px; display: flex; align-items: center; gap: 12px; }
  .brand__dot { width: 34px; height: 34px; border-radius: 50%; background: var(--yellow); flex: none; }
  .brand__name {
    font-family: var(--display); font-size: 20px; line-height: 22px;
    color: var(--navy); font-weight: 400;
  }
  .contact { position: absolute; color: var(--navy); font-weight: 600; font-size: 15px; line-height: 19.5px; }
  .card--front .contact { left: 292px; top: 50px; }
  .tagline { position: absolute; left: 41px; top: 192px; }
  .tagline__title { font-family: var(--display); font-size: 18px; color: var(--yellow); font-weight: 400; margin-bottom: 4px; }
  .tagline__text { font-size: 15px; line-height: 20px; color: var(--band-text); font-weight: 500; }

  /* back */
  .portrait {
    position: absolute; left: 42px; top: 21px; width: 168px; height: 168px;
    border-radius: 50%; background: var(--paper);
  }
  .portrait__photo {
    position: absolute; inset: 0; border-radius: 50%;
    background: radial-gradient(circle at 50% 42%, #c99a7c 0%, #8a5a3e 45%, #3b2a20 80%, var(--paper) 81%);
  }
  .person { position: absolute; left: 262px; top: 28px; }
  .person__name { font-family: var(--display); font-size: 20px; color: var(--yellow); font-weight: 400; line-height: 22px; }
  .person__role { font-size: 15px; color: var(--band-text); font-weight: 500; line-height: 18px; }
  .card--back .contact { left: 262px; top: 76px; color: var(--band-text); font-weight: 500; }
  .credentials {
    position: absolute; left: 40px; top: 206px; right: 30px;
    font-size: 16px; line-height: 21px; color: var(--navy); font-weight: 600;
  }
</style>
</head>
<body>
<div class="canvas">
  <section class="card card--front">
    <div class="brand">
      <span class="brand__dot"></span>
      <span class="brand__name">Brightpath Learning<br>Consultancy</span>
    </div>
    <div class="contact">
      www.brightpathlearn.nz<br>
      info@brightpathlearn.nz<br>
      phone +64 09 37 615 48
    </div>
    <div class="band"></div>
    <div class="tagline">
      <p class="tagline__title">Brightpath Learning Consultancy</p>
      <p class="tagline__text">We use Child-Centred, Modern and Innovative approaches<br>Teaching autistic children to bond, laugh and play</p>
    </div>
  </section>

  <section class="card card--back">
    <div class="band"></div>
    <div class="portrait">
      <div class="portrait__photo" role="img" aria-label="Portrait photo of the founder"></div>
    </div>
    <div class="person">
      <p class="person__name">Mirela Dunstan</p>
      <p class="person__role">Founder</p>
    </div>
    <div class="contact">
      phone:&nbsp; +64 937 615 48<br>
      mobile: +64 20 6283 9150<br>
      mirela@brightpathlearn.nz
    </div>
    <p class="credentials">
      Postgraduate Autism (Children) Specialist (with Merit)<br>
      Qualified by the Faculty of Learning Support and Access<br>
      Studies (FLSA), Harwell Vale University
    </p>
  </section>
</div>
</body>
</html>
```